Criação de Papelaria Profissional para Advocacia e Direito
A empresa queria:
" Ribeiro Tavares Advogados é um escritório boutique de atuação diversificada (full service) "

```html
<!DOCTYPE html>
<html lang="pt">
<head>
<meta charset="utf-8">
<title>Ribeiro Tavares Advogados — Pasta Institucional</title>
<link rel="stylesheet" href="https://fonts.googleapis.com/css2?family=Montserrat:wght@400&display=swap">
<style>
  :root {
    --backdrop: #e9e7e4;
    --folder-deep: #2c4558;
    --folder-mid: #3b5a70;
    --folder-light: #4a6d84;
    --silver: #d7dcdf;
    --silver-dim: #aeb6bb;
    --paper: #f7f7f6;
    --paper-shade: #e6e7e7;
  }
  html, body {
    margin: 0;
    width: 1200px;
    height: 1200px;
    overflow: hidden;
    background: var(--backdrop);
    font-family: "Montserrat", sans-serif;
  }
  .canvas {
    position: relative;
    width: 1200px;
    height: 1200px;
  }
  .folder-cover {
    position: absolute;
    left: 80px;
    top: 180px;
    width: 500px;
    height: 760px;
    border-radius: 4px 22px 22px 4px;
    background: linear-gradient(120deg, var(--folder-deep) 0%, var(--folder-mid) 55%, var(--folder-light) 100%);
    box-shadow: 0 10px 30px rgba(0,0,0,0.18);
    overflow: hidden;
  }
  .cover-stripe {
    position: absolute;
    left: 0;
    right: 0;
    bottom: 38px;
    height: 10px;
    background: var(--silver-dim);
  }
  .brand {
    position: absolute;
    left: 0;
    right: 0;
    top: 230px;
    text-align: center;
    color: var(--silver);
    font-weight: 400;
  }
  .brand-name {
    font-size: 34px;
    letter-spacing: 0.02em;
    line-height: 1;
  }
  .brand-tagline {
    margin-top: 12px;
    font-size: 13px;
    letter-spacing: 0.04em;
  }
  .folder-inside {
    position: absolute;
    left: 620px;
    top: 180px;
    width: 500px;
    height: 760px;
    background: linear-gradient(180deg, var(--paper) 0%, var(--paper-shade) 100%);
    border-radius: 4px;
    box-shadow: 0 10px 30px rgba(0,0,0,0.14);
    overflow: hidden;
  }
  .pocket {
    position: absolute;
    left: 0;
    bottom: 0;
    width: 500px;
    height: 300px;
  }
  .pocket-brand {
    position: absolute;
    right: 40px;
    bottom: 60px;
    text-align: right;
    color: var(--silver);
    font-weight: 400;
  }
  .pocket-brand .brand-name {
    font-size: 22px;
    letter-spacing: 0.02em;
    line-height: 1;
  }
  .pocket-brand .brand-tagline {
    font-size: 10px;
    margin-top: 8px;
    letter-spacing: 0.04em;
  }
</style>
</head>
<body>
<main class="canvas">
  <section class="folder-cover">
    <div class="brand">
      <div class="brand-name">Ribeiro Tavares</div>
      <div class="brand-tagline">Advocacia · Full Service</div>
    </div>
    <div class="cover-stripe"></div>
  </section>

  <section class="folder-inside">
    <svg class="pocket" viewBox="0 0 500 300" aria-hidden="true">
      <defs>
        <linearGradient id="pocket-fill" x1="0" y1="0" x2="1" y2="1">
          <stop offset="0" stop-color="#3f6a80"/>
          <stop offset="1" stop-color="#2c4a5e"/>
        </linearGradient>
      </defs>
      <polygon points="0,40 500,0 500,300 0,300" fill="url(#pocket-fill)"/>
    </svg>
    <div class="pocket-brand">
      <div class="brand-name">Ribeiro Tavares</div>
      <div class="brand-tagline">Advocacia · Full Service</div>
    </div>
  </section>
</main>
</body>
</html>
```